Portfolio Project

The Portfolio gives you the opportunity to “package” your experience, expertise, and testimonials in a professional brochure-like format. This can be used to present in an interview to discuss you as a “product,” similar to what a salesperson would do when they are presenting their product’s features and benefits.
It’s an impressive way to present yourself as a professional who understands the importance of standing out and making an impactful statement about your skills, talents and success.
The components of this project need to include the following:
I. Resume (I have. No need to do anything with this)
II. Top 3 Features to Summarize You (Leadership/Sales/Driven)
a. These should be dividers in your portfolio that easily highlight your “product offerings”
b. Attributes you would use to describe and promote yourself
c. Make this up and i will ad on. Ex: Marketing, Sales, Training, Customer Service, Project Management, etc.
III. Each Feature must incorporate the following behind it – Do this for EACH Feature
a. Summarize experience – provide summary of what you did – make it quantifiable: numbers, charts, graphs
b. Provide examples: any proof of work, design, projects, etc.
c. Provide testimonials: emails of job well done, communications, etc.
d. Provide awards, certifications, recognitions (I Have)
IV. References ( I have)
a. Include at least two reference letters that will highlight your professional/working experience. (i have)
V. Professionally bind the portfolio (I will do)
Updates

I have increased the budget by $50.

Just a reminder, this is a portfolio to give to someone in a job interview. The finished size will be aprox 10 - 15 pages total. It will include a lot of pictures of me and my accomplishments in the military and school. It will Including my resume and scanned photos of awards that I have received (I will do). What I'm needing from a designer is aprox 10 pages that includes a few of the pictures of me with a nice background and layout. Writing about myself and my accomplishments and goals isn't difficult for me. What I need help with is the format/graphics/layout with places to write about myself and my accomplishments. In the Military (Harbor Guard), in the course for mastery in trading (CMT) at College of Brantwick and with pitch right in (my company) www.pitchrightinhub.example it should be fairly easy for a graphic designer. I have uploaded my resume to this website for your viewing.

I have also uploaded an example of a friends personal portfolio to the website. That is one of the better ones I have seen. THIS IS A GOOD REFERENCE. HIS IS VERY GOOD. 

I DO NOT WANT IT TO "BUSY". THE FOCUS IS ON ME AND MY ACCOMPLISHMENTS.

Once I receive the files I will print and get bonded (like a book or magazine). I would like to be able to interchange pictures on the document as well if possible. So if later on I want to use a different picture or a higher quality picture I can. Please feel free to contact me with ANY questions!

rkmalden71@mailbox.example
001 555 014 7392

Thank You.

Target Market(s)

CEO's,VP's, HR managers

Industry/Entity Type

Leadership

Requirements
Must have
• Please see Example attached.
Nice to have
• If you have ANY questions at all please feel free to e-mail me at rkmalden71@mailbox.example

```html
<!DOCTYPE html>
<html lang="en">
<head>
<meta charset="utf-8">
<title>RK Malden — Personal Portfolio</title>
<link rel="stylesheet" href="https://fonts.googleapis.com/css2?family=Archivo+Black&family=Arimo:wght@400&display=swap">
<style>
  :root {
    --ink: #000000;
    --signal-red: #d7191f;
    --plum: #695169;
    --paper: #ffffff;
    --sage: #b8bf7a;
    --photo-deep: #3a0608;
    --photo-mid: #8e1418;
  }
  html, body {
    margin: 0;
    padding: 0;
    overflow: hidden;
    background: var(--paper);
  }
  .cover {
    position: relative;
    width: 848px;
    height: 1200px;
    overflow: hidden;
    background: var(--paper);
  }
  .block { position: absolute; }
  .swatch-black { left: 0; top: 0; width: 297px; height: 226px; background: var(--ink); }
  .swatch-red { left: 297px; top: 0; width: 279px; height: 226px; background: var(--signal-red); }
  .swatch-plum { left: 576px; top: 0; width: 272px; height: 226px; background: var(--plum); }

  .name-plate {
    position: absolute;
    left: 0;
    top: 290px;
    width: 848px;
    height: 170px;
    overflow: hidden;
  }
  .name-plate text {
    font-family: "Archivo Black", "Arial Black", sans-serif;
    font-size: 182px;
  }
  .name-first { fill: var(--ink); }
  .name-last { fill: var(--signal-red); }

  .objective-panel { left: 0; top: 453px; width: 297px; height: 522px; background: var(--signal-red); }
  .base-panel { left: 0; top: 975px; width: 297px; height: 225px; background: var(--ink); }
  .portrait {
    left: 297px;
    top: 453px;
    width: 551px;
    height: 747px;
    background:
      radial-gradient(ellipse 60% 45% at 60% 35%, var(--photo-mid) 0%, rgba(142,20,24,0) 100%),
      linear-gradient(180deg, #6d0e11 0%, var(--photo-deep) 55%, #120405 100%);
  }

  .objective {
    position: absolute;
    left: 73px;
    top: 507px;
    width: 190px;
  }
  .objective h2 {
    margin: 0 0 6px;
    font-family: "Archivo Black", "Arial Black", sans-serif;
    font-size: 15.5px;
    line-height: 19px;
    text-transform: uppercase;
    color: var(--ink);
    font-weight: 400;
  }
  .strengths {
    list-style: none;
    margin: 0;
    padding: 0;
    font-family: "Arimo", Arial, sans-serif;
    font-size: 13px;
    line-height: 21.5px;
    color: var(--paper);
  }

  .contents {
    position: absolute;
    right: 203px;
    top: 1030px;
    margin: 0;
    padding: 0;
    list-style: none;
    text-align: right;
    font-family: "Archivo Black", "Arial Black", sans-serif;
    font-size: 32px;
    line-height: 43px;
    text-transform: uppercase;
    white-space: nowrap;
  }
  .contents .resume, .contents .testimonials { color: var(--paper); }
  .contents .goals { color: var(--sage); }

  .accent-square { left: 670px; top: 1037px; width: 131px; height: 118px; background: var(--signal-red); }
</style>
</head>
<body>
<main class="cover">
  <div class="block swatch-black"></div>
  <div class="block swatch-red"></div>
  <div class="block swatch-plum"></div>

  <svg class="name-plate" viewBox="0 290 848 170" aria-label="RK Malden">
    <text x="-14" y="453" textLength="880" lengthAdjust="spacingAndGlyphs"><tspan class="name-first">RK</tspan><tspan class="name-last"> MALDEN</tspan></text>
  </svg>

  <div class="block objective-panel"></div>
  <div class="block base-panel"></div>
  <div class="block portrait" role="img" aria-label="Portrait photo of RK Malden in a dark suit, adjusting his tie, against a red backdrop"></div>

  <section class="objective">
    <h2>Objective:<br>To start a career as a sales representative at Corvell Drilling.</h2>
    <ul class="strengths">
      <li>Top Secret Clearance Sales</li>
      <li>Hiring and Training</li>
      <li>Customer Service</li>
      <li>Business Operations</li>
      <li>Extremely self driven/moti-<br>vated</li>
    </ul>
  </section>

  <ul class="contents">
    <li class="resume">Personal Resume</li>
    <li class="goals">My Motivation and Goals</li>
    <li class="testimonials">My Testimonials</li>
  </ul>

  <div class="block accent-square"></div>
</main>
</body>
</html>
```